Tall Harbor Business Card

We are a Video Production and Video Equipment Rental company specialising in the supply of state of the art Video Technology and Services for the Live Entertainment, Television and Corporate Business Theatre markets. (in Sydney, Australia) www.tallharbor-media.example

Industry/Entity Type

Business

Contact Information for Business Card

name, position, email, website, address, logo
Example attached of the information we need - doesn't necessarily have to look the same

Font styles to use
Other font styles liked:
• Tall Harbor logo font is GOTHAM

Colors
ea1f27

Requirements
Nice to have
• either matt black or shiny black cards -
raised logo

```html
<!DOCTYPE html>
<html lang="en">
<head>
<meta charset="utf-8">
<title>Tall Harbor Business Card</title>
<link rel="stylesheet" href="https://fonts.googleapis.com/css2?family=Open+Sans:wght@400;600&display=swap">
<style>
  :root {
    --stage: #e9e6e2;
    --paper: #ffffff;
    --charcoal: #333333;
    --brand-red: #c8232c;
    --deep-red: #8b1a1e;
    --ink: #1a1a1a;
    --band-shade: rgba(30, 0, 0, 0.55);
  }
  html, body {
    margin: 0;
    width: 1200px;
    height: 960px;
    overflow: hidden;
    background: var(--stage);
  }
  .canvas {
    position: relative;
    width: 1200px;
    height: 960px;
  }
  .card {
    position: absolute;
    top: 185px;
    width: 360px;
    height: 590px;
    box-shadow: 0 14px 30px rgba(0, 0, 0, 0.22);
  }
  .card--front { left: 210px; }
  .card--back { left: 630px; }
  .card svg { display: block; }
  .wordmark {
    font-family: "Open Sans", sans-serif;
    font-weight: 600;
    font-size: 34px;
    letter-spacing: 1px;
    fill: var(--paper);
  }
  .services {
    font-family: "Open Sans", sans-serif;
    font-size: 20px;
    fill: var(--paper);
  }
  .person-name {
    font-family: "Open Sans", sans-serif;
    font-weight: 600;
    font-size: 28px;
    fill: var(--ink);
  }
  .person-role {
    font-family: "Open Sans", sans-serif;
    font-size: 15px;
    fill: var(--ink);
  }
  .contact-line {
    font-family: "Open Sans", sans-serif;
    font-size: 12.5px;
    fill: var(--paper);
  }
  .contact-icon { fill: var(--paper); }
</style>
</head>
<body>
<main class="canvas">

  <section class="card card--front" aria-label="Business card front">
    <svg width="360" height="590" viewBox="0 0 360 590">
      <defs><clipPath id="front-clip"><rect width="360" height="590"/></clipPath></defs>
      <g clip-path="url(#front-clip)">
        <rect class="card-paper" width="360" height="590" fill="var(--paper)"/>
        <rect class="logo-band" y="60" width="360" height="110" fill="var(--charcoal)"/>
        <text class="wordmark" x="180" y="127" text-anchor="middle">TALL HARBOR</text>
        <circle class="accent-circle accent-circle--deep" cx="95" cy="540" r="235" fill="var(--deep-red)"/>
        <circle class="accent-circle accent-circle--red" cx="345" cy="440" r="225" fill="var(--brand-red)"/>
        <rect class="services-band" y="440" width="360" height="88" fill="var(--band-shade)"/>
        <text class="services" x="180" y="477" text-anchor="middle">Video Solutions - LED Screens</text>
        <text class="services" x="180" y="505" text-anchor="middle">Camera Systems - Projection</text>
      </g>
    </svg>
  </section>

  <section class="card card--back" aria-label="Business card back">
    <svg width="360" height="590" viewBox="0 0 360 590">
      <defs><clipPath id="back-clip"><rect width="360" height="590"/></clipPath></defs>
      <g clip-path="url(#back-clip)">
        <rect class="card-paper" width="360" height="590" fill="var(--paper)"/>
        <text class="person-name" x="60" y="205">Sam Whitlock</text>
        <text class="person-role" x="62" y="228">Managing Director</text>
        <circle class="accent-circle accent-circle--dark" cx="80" cy="640" r="215" fill="var(--charcoal)"/>
        <circle class="accent-circle accent-circle--red" cx="370" cy="440" r="235" fill="var(--brand-red)"/>
        <rect class="logo-band" y="345" width="360" height="88" fill="rgba(0,0,0,0.6)"/>
        <text class="wordmark" x="180" y="401" text-anchor="middle">TALL HARBOR</text>

        <g class="contact-block">
          <g class="contact-icon">
            <path d="M70 462a6 6 0 0 1 12 0c0 5-6 11-6 11s-6-6-6-11z"/>
            <circle cx="76" cy="462" r="2" fill="var(--charcoal)"/>
          </g>
          <g class="contact-icon">
            <rect x="69" y="484" width="14" height="10" rx="1"/>
            <path d="M69 485l7 5 7-5" fill="none" stroke="var(--charcoal)" stroke-width="1.2"/>
          </g>
          <g class="contact-icon">
            <circle cx="76" cy="513" r="7"/>
            <path d="M69 513h14M76 506v14M76 506c-4 4-4 10 0 14M76 506c4 4 4 10 0 14" fill="none" stroke="var(--charcoal)" stroke-width="1"/>
          </g>
          <text class="contact-line" x="96" y="468">sam@tallharbor-media.example</text>
          <text class="contact-line" x="96" y="493">www.tallharbor-media.example</text>
          <text class="contact-line" x="96" y="518">12 Wharf Lane Pyrmont NSW 2009 Australia</text>
        </g>
      </g>
    </svg>
  </section>

</main>
</body>
</html>
```